Business Card Design

We need a business card design for a new company located in Missouri City, TX, entitled 'BrightPath Chiropractic & Holistic Center'. Our services include restoration of health and vitality, spinal exam, health assessment, dietary & fitness programs, lymphatic & therapeutic massage, detox & remineralize body wraps, far infrared sauna therapy

Industry/Entity Type

Business

Contact Information for Business Card

BrightPath Chiropractic & Holistic Center, Marlena Oskow LMT, 4512 Hwy. 9, Suite 310, Missouri City, TX 77381, 281-555-0193

```html
<!DOCTYPE html>
<html lang="en">
<head>
<meta charset="utf-8">
<title>BrightPath Chiropractic &amp; Holistic Center – Business Card</title>
<link href="https://fonts.googleapis.com/css2?family=Marcellus&family=Merriweather:wght@700&display=swap" rel="stylesheet">
<style>
  :root {
    --bg: #3a3a3a;
    --card: #232425;
    --lime: #c8e06c;
    --pink: #ec6aa8;
    --white: #f4f4f4;
    --faint: #3b3f37;
  }
  * { margin: 0; padding: 0; box-sizing: border-box; }
  html, body { width: 1200px; height: 1189px; overflow: hidden; }
  body {
    background: var(--bg);
    font-family: "Marcellus", serif;
    color: var(--white);
    position: relative;
  }
  .card {
    position: absolute;
    left: 150px;
    width: 900px;
    height: 514px;
    background: var(--card);
    border-radius: 28px;
    box-shadow: 0 14px 40px rgba(0,0,0,.45);
    overflow: hidden;
  }
  .card--back { top: 48px; }
  .card--front { top: 626px; }

  /* back */
  .services { position: absolute; left: 100px; top: 110px; }
  .services__title {
    color: var(--lime);
    font-size: 28px;
    letter-spacing: 1px;
    margin-bottom: 8px;
  }
  .services__list { list-style: none; }
  .services__list li {
    font-size: 24px;
    line-height: 38px;
    display: flex;
    align-items: center;
  }
  .services__list li::before {
    content: "";
    width: 14px; height: 14px;
    border-radius: 50%;
    background: var(--pink);
    margin-right: 16px;
  }
  .services__list li:first-child::before { background: transparent; }
  .back-mark {
    position: absolute;
    right: 60px; top: 30px;
    width: 310px; height: 310px;
    border-radius: 50%;
    background: var(--faint);
    display: flex; align-items: center; justify-content: center;
    color: #4d5346;
    font-size: 40px;
  }

  /* front */
  .brand-mark {
    position: absolute;
    left: 70px; top: 95px;
    width: 190px; height: 190px;
    border-radius: 50%;
    background: radial-gradient(circle at 50% 45%, #e8f3b8, #b6d35c);
    display: flex; align-items: center; justify-content: center;
    color: #d2478c;
    font-size: 28px;
  }
  .divider-v {
    position: absolute;
    left: 300px; top: 70px;
    width: 2px; height: 240px;
    background: var(--lime);
  }
  .company {
    position: absolute;
    left: 335px; top: 115px;
    color: var(--lime);
    font-size: 36px;
    line-height: 46px;
    letter-spacing: 1px;
  }
  .person {
    position: absolute;
    right: 60px; top: 215px;
    text-align: right;
  }
  .person__name {
    font-family: "Merriweather", serif;
    font-weight: 700;
    font-size: 34px;
  }
  .person__role {
    color: var(--lime);
    font-size: 23px;
    letter-spacing: 1px;
  }
  .rule {
    position: absolute;
    left: 110px; top: 305px;
    width: 530px; height: 2px;
    background: var(--lime);
  }
  .address {
    position: absolute;
    right: 60px; top: 345px;
    text-align: right;
    font-size: 24px;
    line-height: 32px;
    letter-spacing: .5px;
  }
  .contact { position: absolute; left: 110px; top: 395px; list-style: none; }
  .contact li {
    display: flex; align-items: center;
    font-size: 28px;
    line-height: 44px;
    letter-spacing: .5px;
  }
  .contact svg { width: 32px; height: 32px; margin-right: 14px; }
</style>
</head>
<body>

<section class="card card--back" aria-label="Card back">
  <div class="back-mark">BrightPath</div>
  <div class="services">
    <h2 class="services__title">OUR SERVICES</h2>
    <ul class="services__list">
      <li>restoration of health and vitality</li>
      <li>spinal exam</li>
      <li>health assessment</li>
      <li>dietary &amp; fitness programs</li>
      <li>lymphatic &amp; therapeutic massage</li>
      <li>detox &amp; remineralize body wraps</li>
      <li>far infrared sauna therapy</li>
    </ul>
  </div>
</section>

<section class="card card--front" aria-label="Card front">
  <div class="brand-mark">BrightPath</div>
  <div class="divider-v"></div>
  <h1 class="company">BrightPath Chiropractic<br>&amp; Holistic Center</h1>
  <div class="person">
    <div class="person__name">Marlena Oskow LMT</div>
    <div class="person__role">Managing Director</div>
  </div>
  <div class="rule"></div>
  <address class="address" style="font-style:normal">4512 Hwy. 9, Suite 310,<br>Missouri City,TX 77381</address>
  <ul class="contact">
    <li>
      <svg viewBox="0 0 32 32" aria-hidden="true"><rect width="32" height="32" rx="4" fill="#ec6aa8"/><path d="M11 8c1 0 2 3 2 4s-2 1-2 2 3 5 5 6 1-2 2-2 4 1 4 2-1 3-3 3C12 23 8 15 8 11c0-2 2-3 3-3z" fill="#232425"/></svg>
      281-555-0193
    </li>
    <li>
      <svg viewBox="0 0 32 32" aria-hidden="true"><rect width="32" height="32" rx="4" fill="#ec6aa8"/><rect x="7" y="10" width="18" height="13" fill="none" stroke="#232425" stroke-width="2"/><path d="M7 10l9 7 9-7" fill="none" stroke="#232425" stroke-width="2"/></svg>
      yourcompany@brightpathmail.com
    </li>
  </ul>
</section>

</body>
</html>
```